Law practice business card

I have an existing logo that I would like to make a little cleaner and maybe something more creative, but using the same base. I would like a contempoary design of the business card.

Industry/Entity Type

Law

Logo Text

On one side of the card - below the logo - I would want to say "BRANTOVE" and below that it should read "LAW OFFICES, PC" in smaller print. If you have somethign more creative, I would love to see it.

Logo styles of interest
Lettermark Logo
Font styles to use
Sans Serif

Colors

Designer to choose only greyscale colors for use in the design.

Requirements
Must have
• Standard info: My name with "Attorney at Law" underneath; phone, fax, address, email and website.

```html
<!DOCTYPE html>
<html lang="en">
<head>
<meta charset="utf-8">
<title>Brantove Law Offices, PC — Identity &amp; Business Card</title>
<link rel="stylesheet" href="https://fonts.googleapis.com/css2?family=Poppins:wght@400;500;600&display=swap">
<style>
  :root {
    --maroon: #3a1519;
    --ink: #120a0b;
    --black: #0d0d0d;
    --white: #ffffff;
    --stage: #1e2630;
    --muted: #5a3a3d;
  }
  * { margin: 0; padding: 0; box-sizing: border-box; }
  html, body { width: 1200px; height: 1200px; overflow: hidden; }
  body {
    font-family: "Poppins", sans-serif;
    background: var(--white);
    position: relative;
  }

  /* Brand lockup */
  .brand-panel {
    position: absolute; left: 0; top: 0;
    width: 1200px; height: 436px;
    background: var(--white);
    display: flex; flex-direction: column; align-items: center;
    padding-top: 118px;
  }
  .brand-square {
    width: 84px; height: 84px;
    background: var(--maroon);
    margin-bottom: 40px;
  }
  .brand-name {
    font-size: 70px; font-weight: 600; line-height: 1;
    color: var(--maroon); letter-spacing: 0.01em;
  }
  .brand-descriptor {
    margin-top: 14px;
    font-size: 30px; font-weight: 400; line-height: 1;
    color: var(--black); letter-spacing: 0.16em;
  }

  /* Card presentation area */
  .card-panel {
    position: absolute; left: 0; top: 436px;
    width: 1200px; height: 764px;
    background: var(--stage);
  }
  .card {
    position: absolute; top: 250px;
    width: 480px; height: 276px;
    overflow: hidden;
  }
  .card--front { left: 90px; background: var(--maroon); }
  .card--back { left: 630px; }

  .front-lockup {
    position: absolute; inset: 0;
    display: flex; flex-direction: column; align-items: center; justify-content: center;
    color: var(--white);
  }
  .front-lockup .front-square {
    width: 34px; height: 34px; background: var(--white); margin-bottom: 14px;
  }
  .front-lockup .front-name { font-size: 36px; font-weight: 600; line-height: 1; }
  .front-lockup .front-descriptor {
    font-size: 14px; letter-spacing: 0.16em; margin-top: 6px; line-height: 1;
  }

  .back-art { position: absolute; inset: 0; }

  .back-firm {
    position: absolute; left: 150px; top: 30px; width: 200px;
    text-align: center; color: var(--maroon);
  }
  .back-firm .firm-square {
    width: 18px; height: 18px; background: var(--maroon); margin: 0 auto 8px;
  }
  .back-firm .firm-name { font-size: 22px; font-weight: 600; line-height: 1; }
  .back-firm .firm-descriptor { font-size: 9px; letter-spacing: 0.14em; margin-top: 3px; color: var(--black); }

  .back-person {
    position: absolute; left: 130px; top: 116px;
    color: var(--white);
  }
  .back-person .person-name { font-size: 24px; font-weight: 600; line-height: 1; }
  .back-person .person-title { font-size: 9px; letter-spacing: 0.14em; margin-top: 3px; }

  .contact-list {
    position: absolute; left: 130px; top: 170px;
    list-style: none;
    font-size: 11px; color: var(--muted); line-height: 1;
  }
  .contact-list li {
    display: flex; align-items: center; gap: 8px; height: 18px;
  }
  .contact-list svg { width: 10px; height: 10px; fill: var(--ink); flex: none; }
</style>
</head>
<body>

<section class="brand-panel">
  <div class="brand-square"></div>
  <div class="brand-name">BRANTOVE</div>
  <div class="brand-descriptor">LAW OFFICES, PC</div>
</section>

<section class="card-panel">
  <article class="card card--front">
    <div class="front-lockup">
      <div class="front-square"></div>
      <div class="front-name">BRANTOVE</div>
      <div class="front-descriptor">LAW OFFICES, PC</div>
    </div>
  </article>

  <article class="card card--back">
    <svg class="back-art" viewBox="0 0 480 276" aria-hidden="true">
      <rect width="480" height="276" fill="#3a1519"/>
      <polygon points="0,40 120,40 70,276 0,276" fill="#120a0b"/>
      <polygon points="120,0 440,0 380,108 95,108" fill="#ffffff"/>
      <polygon points="85,160 400,160 460,276 60,276" fill="#ffffff"/>
    </svg>

    <div class="back-firm">
      <div class="firm-square"></div>
      <div class="firm-name">BRANTOVE</div>
      <div class="firm-descriptor">LAW OFFICES, PC</div>
    </div>

    <div class="back-person">
      <div class="person-name">BRANTOVE</div>
      <div class="person-title">ATTORNEY AT LAW</div>
    </div>

    <ul class="contact-list">
      <li><svg viewBox="0 0 10 10"><path d="M2 0h2l1 3-1.5 1a6 6 0 0 0 2.5 2.5L7 5l3 1v2c0 1-1 2-2 2A8 8 0 0 1 0 2c0-1 1-2 2-2z"/></svg>555 0142 7788</li>
      <li><svg viewBox="0 0 10 10"><rect x="2" y="0" width="6" height="3"/><rect x="0" y="3.5" width="10" height="4" rx="1"/><rect x="2" y="8" width="6" height="2"/></svg>555 0199 3</li>
      <li><svg viewBox="0 0 10 10"><path d="M5 0a3.5 3.5 0 0 1 3.5 3.5C8.5 6 5 10 5 10S1.5 6 1.5 3.5A3.5 3.5 0 0 1 5 0zm0 2a1.5 1.5 0 1 0 0 3 1.5 1.5 0 0 0 0-3z"/></svg>1820 Harlow Ave Ste 210</li>
      <li><svg viewBox="0 0 10 10"><path d="M0 2h10v6H0zM0 2l5 3.5L10 2" stroke="#fff" stroke-width="0.8"/></svg>brantove@mail.com</li>
      <li><svg viewBox="0 0 10 10"><circle cx="5" cy="5" r="5"/><path d="M0 5h10M5 0c-2 3-2 7 0 10M5 0c2 3 2 7 0 10" stroke="#fff" stroke-width="0.7" fill="none"/></svg>brantove.com</li>
    </ul>
  </article>
</section>

</body>
</html>
```